ALL TEXT GRAPHICS TM May 2025 for Instagram

We are looking for a series of social media graphics for Instagram (new size: 4:5 (1080 x 1350 pixels) ratio that are ALL TEXT. We want the following quotes below on each graphic; one quote per graphic. AND, In very small letters at the bottom of each graphic, add @TovaMarshOnline
The look and feel of these graphics should be complimentary to the color palette attached below; but keep them simple. But the design is up to you; at the end of this document, I provided various samples of all text graphics that I like as examples.
Target Market(s)
women looking to lose weight
Look and feel

```html
<!DOCTYPE html>
<html lang="en">
<head>
<meta charset="utf-8">
<title>Flat Tummy in Your 40s — TM</title>
<link rel="stylesheet" href="https://fonts.googleapis.com/css2?family=Libre+Baskerville&family=Poppins:wght@600&display=swap">
<style>
  :root {
    --paper: #ffffff;
    --ink: #111111;
    --pink: #ff35a0;
    --on-pink: #ffffff;
  }
  html, body {
    margin: 0;
    padding: 0;
    overflow: hidden;
    background: var(--paper);
  }
  .post {
    position: relative;
    width: 960px;
    height: 1200px;
    background: var(--paper);
    overflow: hidden;
    font-family: "Libre Baskerville", Baskerville, serif;
    color: var(--ink);
  }
  .bracket {
    position: absolute;
    left: 0;
    top: 0;
  }
  .headline {
    position: absolute;
    left: 89px;
    top: 255px;
    margin: 0;
    font-size: 58px;
    line-height: 84px;
    font-weight: 400;
    letter-spacing: -0.5px;
  }
  .cta-lead {
    position: absolute;
    left: 89px;
    top: 572px;
    margin: 0;
    font-size: 60px;
    line-height: 84px;
  }
  .keyword-band {
    position: absolute;
    left: 88px;
    top: 659px;
    width: 797px;
    height: 133px;
    background: var(--pink);
    box-sizing: border-box;
    padding-left: 41px;
    padding-top: 6px;
    color: var(--on-pink);
    font-size: 74px;
    line-height: 127px;
    letter-spacing: 1px;
  }
  .cta-benefit {
    position: absolute;
    left: 89px;
    top: 815px;
    margin: 0;
    font-size: 54px;
    line-height: 86px;
    letter-spacing: 0.5px;
  }
  .handle {
    position: absolute;
    left: 0;
    width: 960px;
    top: 1128px;
    text-align: center;
    font-family: "Poppins", Arial, sans-serif;
    font-weight: 600;
    font-size: 32px;
    line-height: 42px;
    color: var(--pink);
  }
</style>
</head>
<body>
  <main class="post">
    <svg class="bracket" width="960" height="600" viewBox="0 0 960 600" aria-hidden="true">
      <path d="M 400 205 H 88 A 36 36 0 0 0 52 241 V 505" fill="none" stroke="var(--pink)" stroke-width="3.5"/>
      <polygon points="386,205 418,180 450,205 418,230" fill="var(--pink)"/>
      <polygon points="52,496 77,527 52,558 27,527" fill="var(--pink)"/>
    </svg>

    <h1 class="headline">Falt tummy in your<br>40s? It’s still possible!</h1>

    <p class="cta-lead">Comment</p>
    <div class="keyword-band">BYE BELLY</div>
    <p class="cta-benefit">to get the 10 secrets to a<br>flatter tummy</p>

    <div class="handle">@TovaMarshOnline</div>
  </main>
</body>
</html>
```